Kivora....... a hint of Calm

I need a web design for a new business based in London that will be mobile (offered at homes, parks or a local cafe ect) called Kivora. I offer Life Coaching/Counselling sessions, Personal training, Massage and Sports Massage. Sessions range from an hour to half and hour. My aim is to help people along their journey to help give them gain clarity of where there going, helping them to towards their goals, so that can experience bliss. My website should represent a place people can come to release their stress and worries so that they leave feeling lighter, clearer and happier. I would like my website to reflect someone feeling ALIVE. I would also like a logo design for Kivora with a sentence underneath or near saying a touch of bliss.

Target Market(s)

middle class people

Industry/Entity Type

Business

Coding

Coded - Design and coding required

Number of Pages Required

4 page

Requirements
Must have
• 1st page About us
• 2nd page Services
• 3rd page Prices
• 4th page contact details
Nice to have
• mixture of cultures in images

```html
<!DOCTYPE html>
<html lang="en">
<head>
<meta charset="utf-8">
<title>Kivora — a hint of Calm</title>
<link rel="stylesheet" href="https://fonts.googleapis.com/css2?family=Lato:ital,wght@0,300;0,400;0,700;1,300&display=swap">
<style>
:root{
  --white:#ffffff;
  --ink:#3a3a3a;
  --muted:#9a9a9a;
  --rule:#ececec;
  --sky-top:#3f86b0;
  --sky-mid:#7fb6cc;
  --field-light:#b8955a;
  --field-dark:#4a3620;
  --cloud:#d9dcdc;
  --wheat:#a58a3c;
  --wheat-dark:#3d2a18;
  --dark-btn:#2c2218;
}
*{box-sizing:border-box;margin:0;padding:0}
html,body{width:1200px;height:2961px;overflow:hidden}
body{font-family:'Lato',sans-serif;color:var(--ink);background:var(--white);position:relative}
.abs{position:absolute}
.center{text-align:center}

/* Hero */
.hero{position:absolute;left:0;top:0;width:1200px;height:559px;
  background:linear-gradient(180deg,var(--sky-top) 0%,var(--sky-mid) 38%,var(--field-light) 62%,var(--field-dark) 100%)}
.nav-brand{left:146px;top:14px;font-size:21px;font-weight:400;color:var(--white)}
.nav-links{right:150px;top:18px;display:flex;gap:28px;list-style:none}
.nav-links li{font-size:14px;font-weight:300;color:var(--white)}
.hero-title{left:0;width:1200px;top:186px;font-size:44px;font-weight:400;color:var(--white);letter-spacing:1px}
.hero-tagline{left:0;width:1200px;top:248px;font-size:22px;font-weight:400;color:var(--white);letter-spacing:1px}
.hero-button{left:494px;top:316px;width:207px;height:69px;border:2px solid var(--white);
  color:var(--white);font-size:24px;font-weight:300;display:flex;align-items:center;justify-content:center}
.hero-scroll{left:573px;top:447px;width:54px;height:54px;border-radius:50%;background:var(--dark-btn);
  display:flex;align-items:center;justify-content:center}

/* Services */
.service{width:300px;text-align:center}
.service-icon{width:88px;height:88px;border:2px solid var(--ink);border-radius:50%;margin:0 auto;
  display:flex;align-items:center;justify-content:center}
.service-title{font-size:22px;font-weight:400;margin-top:8px}
.service-text{font-size:13px;font-weight:300;color:var(--muted);line-height:19px;margin:10px auto 0;width:276px}
.service-text + .service-text{margin-top:19px}
.divider{left:144px;top:1007px;width:912px;height:1px;background:var(--rule)}

/* About */
.section-title{left:0;width:1200px;font-size:22px;font-weight:400}
.about-text{left:452px;width:296px;font-size:13.5px;font-weight:300;color:var(--muted);line-height:19px;text-align:center}

/* Quote band */
.quote-band{left:0;top:1540px;width:1200px;height:460px;
  background:linear-gradient(180deg,var(--cloud) 0%,#c9cccb 38%,#6c6a45 42%,var(--wheat) 55%,#8a6a2c 80%,var(--wheat-dark) 100%)}
.avatar{left:537px;top:1631px;width:126px;height:126px;border-radius:50%;background:#8a6a52;border:3px solid #efe7dc}
.quote{left:0;width:1200px;font-size:21px;font-style:italic;font-weight:300;color:var(--white)}
.quote-author{left:0;width:1200px;top:1881px;font-size:12px;color:var(--white)}

/* How we work */
.step{width:300px;text-align:center}
.step-title{font-size:22px;font-weight:400}
.step-text{font-size:13.5px;font-weight:300;color:var(--muted);line-height:19px;margin:16px auto 0;width:292px}

/* Contact band */
.contact-band{left:0;top:2458px;width:1200px;height:286px;
  background:linear-gradient(180deg,var(--sky-top) 0%,var(--sky-mid) 30%,var(--field-light) 60%,var(--field-dark) 100%)}
.contact-title{left:0;width:1200px;top:2512px;font-size:22px;font-weight:700;color:var(--white)}
.contact-line{left:0;width:1200px;font-size:12px;color:var(--white)}

/* Footer */
.footer-brand{left:144px;top:2771px;font-size:22px;font-weight:400;color:var(--ink)}
.footer-links{left:144px;top:2829px;list-style:none}
.footer-links li{font-size:12px;font-weight:300;color:var(--muted);line-height:30px}
</style>
</head>
<body>

<header class="hero" role="img" aria-label="Blurred photo of tall golden grasses under a blue summer sky"></header>
<div class="abs nav-brand">Kivora</div>
<ul class="abs nav-links">
  <li>Life Coaching/Counseling</li>
  <li>Personal Training</li>
  <li>(Sports) Massage</li>
  <li>Contact</li>
</ul>
<h1 class="abs hero-title center">Kivora</h1>
<p class="abs hero-tagline center">a hint of Calm</p>
<div class="abs hero-button">Get Started</div>
<div class="abs hero-scroll">
  <svg width="20" height="14" viewBox="0 0 20 14"><path d="M3 3 L10 10 L17 3" fill="none" stroke="#fff" stroke-width="3" stroke-linecap="round" stroke-linejoin="round"/></svg>
</div>

<section>
  <div class="abs service" style="left:136px;top:653px">
    <div class="service-icon">
      <svg width="30" height="26" viewBox="0 0 30 26"><ellipse cx="12" cy="10" rx="11" ry="8" fill="#3a3a3a"/><path d="M5 15 L3 22 L11 17Z" fill="#3a3a3a"/><ellipse cx="20" cy="15" rx="9" ry="7" fill="#3a3a3a" stroke="#fff" stroke-width="2"/></svg>
    </div>
    <h2 class="service-title">Life Coaching/ Counseling</h2>
    <p class="service-text">Look around joyful bounteous rainbow keenness smile mellow spirit hoopla. Whimsical elated pleasing energy smile bouncy vacation lavender puppy dreaming cheerful dynamic might.</p>
  </div>
  <div class="abs service" style="left:450px;top:653px">
    <div class="service-icon">
      <svg width="24" height="30" viewBox="0 0 24 30"><circle cx="12" cy="4" r="3.5" fill="#3a3a3a"/><path d="M2 6 L8 11 L8 28 L11 28 L12 19 L13 28 L16 28 L16 11 L22 6" fill="#3a3a3a" stroke="#3a3a3a" stroke-width="2" stroke-linejoin="round"/></svg>
    </div>
    <h2 class="service-title">Personal Training</h2>
    <p class="service-text">Laugh juice friendly lenient vigor courteous joyful chipper cooperative philanthropic tree.</p>
    <p class="service-text">Eagerness hold peace giggling effectiveness alert mild yearning moonrise overjoyed happy face energy might sprightly inhabit.</p>
  </div>
  <div class="abs service" style="left:762px;top:653px">
    <div class="service-icon">
      <svg width="26" height="18" viewBox="0 0 26 18"><rect x="1" y="2" width="21" height="14" rx="2" fill="#3a3a3a"/><rect x="22" y="6" width="3" height="6" fill="#3a3a3a"/><path d="M7 9 H15 M11 5 V13" stroke="#fff" stroke-width="2"/></svg>
    </div>
    <h2 class="service-title">(Sports) Massage</h2>
    <p class="service-text">Discover spirited fire going moonrise vivacity mild yearning moonrise overjoyed happy face energy lavender agility vim alive.</p>
  </div>
</section>

<div class="abs divider"></div>

<section>
  <h2 class="abs section-title center" style="top:1110px">Who are we?</h2>
  <p class="abs about-text" style="top:1154px">Lorem ipsum dolor sit amet, consectetuer adipiscing elit. Aenean commodo ligula eget dolor. Aenean massa. Cum sociis natoque penatibus et magnis dis parturient montes, nascetur ridiculus mus. Donec quam felis, ultricies nec, pellentesque eu, pretium quis, sem. Nulla consequat massa quis enim.</p>
  <p class="abs about-text" style="top:1306px">Lorem ipsum dolor sit amet, consectetuer adipiscing elit. Aenean commodo ligula eget dolor. Aenean massa. Cum sociis natoque penatibus et magnis dis parturient montes, nascetur ridiculus mus. Donec quam felis, ultricies nec, pellentesque eu, pretium quis, sem. Nulla consequat massa quis enim.</p>
</section>

<section>
  <div class="abs quote-band" role="img" aria-label="Photo of a wide wheat field under a cloudy sky"></div>
  <div class="abs avatar" role="img" aria-label="Portrait photo of the coach"></div>
  <p class="abs quote center" style="top:1786px">"Eventually everything connects - people, ideas, objects.</p>
  <p class="abs quote center" style="top:1834px">The quality of the connections is the key to quality per se."</p>
  <p class="abs quote-author center">Marlow Finch</p>
</section>

<section>
  <h2 class="abs section-title center" style="top:2101px">How We Work</h2>
  <div class="abs step" style="left:136px;top:2182px">
    <h3 class="step-title">Goals</h3>
    <p class="step-text">Lorem ipsum dolor sit amet, consectetuer adipiscing elit. Aenean commodo ligula eget dolor. Aenean massa. Cum sociis natoque penatibus et magnis dis parturient montes, nascetur ridiculus mus. Donec quam felis, ultricies nec, pellentesque eu, pretium quis, sem. Nulla consequat massa quis enim.</p>
  </div>
  <div class="abs step" style="left:450px;top:2182px">
    <h3 class="step-title">Sessions</h3>
    <p class="step-text">Lorem ipsum dolor sit amet, consectetuer adipiscing elit. Aenean commodo ligula eget dolor. Aenean massa. Cum sociis natoque penatibus et magnis dis parturient montes, nascetur ridiculus mus. Donec quam felis, ultricies nec, pellentesque eu, pretium quis, sem. Nulla consequat massa quis enim.</p>
  </div>
  <div class="abs step" style="left:762px;top:2182px">
    <h3 class="step-title">Happiness</h3>
    <p class="step-text">Lorem ipsum dolor sit amet, consectetuer adipiscing elit. Aenean commodo ligula eget dolor. Aenean massa. Cum sociis natoque penatibus et magnis dis parturient montes, nascetur ridiculus mus. Donec quam felis, ultricies nec, pellentesque eu, pretium quis, sem. Nulla consequat massa quis enim.</p>
  </div>
</section>

<section>
  <div class="abs contact-band" role="img" aria-label="Blurred photo of golden grasses under a blue sky"></div>
  <h2 class="abs contact-title center">Contact Us</h2>
  <p class="abs contact-line center" style="top:2558px">Kivora</p>
  <p class="abs contact-line center" style="top:2576px">18 Larch Lane</p>
  <p class="abs contact-line center" style="top:2594px">Holloway Vale, LN 40218</p>
  <p class="abs contact-line center" style="top:2633px">+44 7700 900411</p>
  <p class="abs contact-line center" style="top:2651px">info@kivora.co.uk</p>
</section>

<footer>
  <div class="abs footer-brand">Kivora</div>
  <ul class="abs footer-links">
    <li>Life Coaching/Counseling</li>
    <li>Personal Training</li>
    <li>(Sports) Massage</li>
    <li>Contact Us</li>
  </ul>
</footer>

</body>
</html>
```